13 Tovi - new website design project

Our company Tovi Electrical is developing a new lead generation website focused on Electrical, LED Lighting and Solar Power. We need a high converting website.

Example of our current website is www.tovielectrical.com.au You can take content from this website for this new design. Our colours are red, black and white. For our new website we would like to promote Tovi, Bright Days Ahead. Please listen to the jingle.

The below link is the company jingle that we have developed.
http://www.tunecraftstudio.com.au/tov-tc-v1/

The key for this brief is to generate leads for Electrical, LED Lighting (for commercial) and Solar Power & Storage.

Target Market(s)

Business owners in Melbourne Victoria

Number of Pages Required

4 page

Colors
ec1f27
ffffff

Requirements
Must have
• This page must be clean, be in line with company branding and a high converting lead website.

```html
<!DOCTYPE html>
<html lang="en">
<head>
<meta charset="utf-8">
<title>Tovi Electrical</title>
<link href="https://fonts.googleapis.com/css2?family=Open+Sans:wght@400;600;700&display=swap" rel="stylesheet">
<style>
:root{
  --red:#ec1f27;
  --ink:#1e1f24;
  --text:#555a60;
  --muted:#8a8e93;
  --line:#d5d7da;
  --light:#f4f4f5;
  --nav:#2e3139;
  --foot:#2b2d36;
  --foot-deep:#1f2027;
  --white:#ffffff;
}
*{box-sizing:border-box;margin:0;padding:0}
html,body{width:1200px;height:3041px;overflow:hidden}
body{font-family:'Open Sans',sans-serif;color:var(--text);background:var(--white);font-size:12px}
a{color:inherit;text-decoration:none}
.wrap{width:888px;margin:0 auto;position:relative}

/* top bar */
.topbar{height:30px;border-bottom:1px solid #e6e6e6;font-size:10px;color:var(--ink)}
.topbar .wrap{display:flex;justify-content:space-between;align-items:center;height:30px}
.topbar .social{display:flex;gap:8px;align-items:center}
.topbar .social span{width:8px;height:8px;border-radius:50%;background:var(--ink);display:inline-block}

/* header */
.header{height:82px}
.header .wrap{display:flex;justify-content:space-between;align-items:center;height:82px}
.brand{display:flex;align-items:center;gap:10px;font-size:34px;font-weight:700;color:var(--ink)}
.brand i{width:26px;height:26px;border-radius:50%;background:var(--red);display:block}
.contacts{display:flex;gap:44px}
.contact{display:flex;align-items:center;gap:12px;font-size:11px;line-height:15px;color:var(--ink)}
.contact .ring{width:40px;height:40px;border:1px solid var(--red);border-radius:50%;display:flex;align-items:center;justify-content:center}

/* nav */
.nav{height:46px;background:var(--nav)}
.nav ul{list-style:none;display:flex;justify-content:center;gap:52px;padding-left:110px;height:46px;align-items:center}
.nav li{color:var(--white);font-size:11px;font-weight:600;position:relative;padding-top:12px}
.nav li::before{content:"";position:absolute;top:0;left:50%;margin-left:-2px;width:4px;height:8px;background:var(--white);clip-path:polygon(0 0,100% 0,100% 60%,50% 100%,0 60%)}
.nav li.active{color:var(--red)}
.nav li.active::before{background:var(--red)}

/* hero */
.hero{height:438px;position:relative;background:linear-gradient(180deg,#5a1a1c 0%,#6b2426 40%,#3b3033 75%,#2c2a30 100%);text-align:center;color:var(--white)}
.hero .photo{position:absolute;inset:0}
.hero h1{position:absolute;top:216px;left:0;right:0;font-weight:400;font-size:24px;line-height:30px}
.hero h1 em{font-style:normal;color:var(--red);font-weight:600}
.hero .actions{position:absolute;top:290px;left:0;right:0;display:flex;justify-content:center;gap:22px}
.btn{display:inline-flex;align-items:center;justify-content:center;gap:6px;height:30px;padding:0 22px;font-size:11px;border:1px solid var(--ink);color:var(--ink);background:var(--white)}
.btn.ghost{background:transparent;border-color:var(--white);color:var(--white)}
.btn.solid{background:var(--red);border-color:var(--red);color:var(--white)}

/* section heading */
.sec-title{display:flex;align-items:center;justify-content:center;gap:16px;color:var(--red);font-size:23px;font-weight:600}
.sec-title::before,.sec-title::after{content:"";width:140px;height:1px;background:var(--line)}

/* story */
.story{height:676px;padding-top:60px;text-align:center}
.story p{width:650px;margin:30px auto 0;font-size:11px;line-height:17px}
.story .btn{margin-top:24px}
.cards{display:flex;justify-content:space-between;margin-top:52px}
.card{width:280px;height:320px;position:relative}
.card .label{position:absolute;left:50px;right:50px;bottom:44px;height:40px;background:var(--white);border:1px solid var(--line);display:flex;align-items:center;justify-content:center;font-size:14px;font-weight:600;color:var(--ink)}
.card .label.hot{background:var(--red);color:var(--white);border-color:var(--red)}

/* why */
.why{height:400px;background:var(--light);padding-top:60px}
.why .wrap{display:flex}
.why .left{width:310px}
.side-title{display:flex;align-items:center;gap:14px;font-size:23px;font-weight:600;color:var(--red)}
.side-title::after{content:"";width:100px;height:1px;background:var(--line)}
.why .left p{font-size:11px;line-height:18px;margin-top:20px}
.ticks{list-style:none;margin-top:18px;font-size:11px;line-height:19px}
.ticks li{display:flex;align-items:center;gap:10px}
.ticks li::before{content:"";width:7px;height:7px;background:var(--red);clip-path:polygon(0 0,100% 50%,0 100%,30% 50%)}
.why .left .btn{margin-top:18px}
.features{display:grid;grid-template-columns:265px 240px;row-gap:46px;margin-left:68px;margin-top:4px}
.feature{display:flex;align-items:center;gap:18px;font-size:12px;color:var(--text)}
.feature .ico{width:56px;height:56px;border-radius:50%;background:var(--nav);display:flex;align-items:center;justify-content:center;flex:none}
.feature.on .ico{background:var(--red)}
.feature.on{color:var(--red)}

/* testimonials */
.clients{height:402px;padding-top:56px;text-align:center}
.avatar{width:92px;height:92px;border-radius:50%;margin:28px auto 0;border:3px solid var(--white);box-shadow:0 0 0 1px var(--line);background:linear-gradient(160deg,#3f5878,#1c2a3d)}
.clients blockquote{width:650px;margin:32px auto 0;font-size:13px;line-height:22px}
.clients .who{margin-top:24px;font-size:12px;color:var(--ink);font-weight:600}
.clients .where{font-size:11px;color:var(--muted);margin-top:2px}
.arrow{position:absolute;top:172px;width:38px;height:38px;border-radius:50%;display:flex;align-items:center;justify-content:center}
.arrow.prev{left:0;border:2px solid var(--ink)}
.arrow.next{right:0;background:var(--red)}

/* works */
.works{height:336px;background:var(--light);padding-top:44px}
.works .head{display:flex;justify-content:space-between;align-items:center;height:34px}
.works .side-title{color:var(--ink)}
.strip{display:flex;margin-top:22px;height:224px}
.strip div{flex:1;position:relative}
.strip .over{position:absolute;inset:0;background:rgba(20,20,24,.55);display:flex;flex-direction:column;align-items:center;justify-content:center;gap:14px;color:var(--white);font-size:14px}

/* more power */
.more{height:330px;padding-top:64px}
.more .wrap{display:flex;justify-content:space-between}
.more .side-title{color:var(--ink)}
.more .side-title em{font-style:normal;color:var(--red)}
.more .ticks{margin-top:22px;line-height:19.5px}
.more .btn{margin-top:24px}
.video{width:244px;height:200px;background:#111;margin-top:-6px;position:relative;color:var(--white)}
.video .bar{position:absolute;top:8px;left:10px;font-size:10px}
.video .screen{position:absolute;top:28px;left:10px;right:10px;bottom:30px;background:var(--white);display:flex;flex-direction:column;align-items:center;justify-content:center;color:var(--red);font-size:30px;font-weight:700}
.video .screen small{font-size:11px;font-weight:600;color:var(--red)}
.video .progress{position:absolute;left:10px;right:10px;bottom:18px;height:2px;background:#555}
.video .progress::before{content:"";display:block;width:18%;height:2px;background:var(--red)}

/* footer */
.footer{height:250px;background:var(--foot);color:#cfd1d5;padding-top:54px}
.footer .wrap{display:flex}
.col h4{font-size:14px;font-weight:400;color:var(--white);margin-bottom:18px}
.col{font-size:11px;line-height:17px}
.links{list-style:none;line-height:20px}
.links li::before{content:"›";margin-right:8px;color:var(--white)}
.links li.active{color:var(--red)}
.col .phone{font-size:18px;color:var(--white);margin:16px 0 8px}
.signup{display:flex;margin-top:22px}
.signup span{width:186px;height:30px;border-radius:15px 0 0 15px;background:#3a3c46;color:#80838b;font-size:10px;padding:0 14px;display:flex;align-items:center}
.signup b{width:44px;height:30px;border-radius:0 15px 15px 0;background:var(--red);display:flex;align-items:center;justify-content:center}
.circles{display:flex;gap:10px}
.circles span{width:30px;height:30px;border-radius:50%;border:1px solid #cfd1d5}
.circles span.on{background:var(--red);border-color:var(--red)}
.bottom{height:51px;background:var(--foot-deep);color:#cfd1d5;font-size:10px}
.bottom .wrap{display:flex;justify-content:space-between;align-items:center;height:51px}
.bottom nav{display:flex;gap:18px}
</style>
</head>
<body>

<div class="topbar"><div class="wrap">
  <span>◷ Opening Times: Mon - Sat 8.00 - 18.00</span>
  <span class="social">Follow Us: <span></span><span></span><span></span></span>
</div></div>

<header class="header"><div class="wrap">
  <div class="brand"><i></i>Tovi</div>
  <div class="contacts">
    <div class="contact">
      <span class="ring"><svg width="16" height="16" viewBox="0 0 16 16"><path d="M1 7 15 1 10 15 7 9Z" fill="none" stroke="#ec1f27" stroke-width="1.4" stroke-linejoin="round"/></svg></span>
      <span>Call Us: +139907<br>service@tovielectrical.com.au</span>
    </div>
    <div class="contact">
      <span class="ring"><svg width="14" height="18" viewBox="0 0 14 18"><path d="M7 17C3 11 1 8.5 1 6a6 6 0 0 1 12 0c0 2.5-2 5-6 11Z" fill="none" stroke="#ec1f27" stroke-width="1.5"/><circle cx="7" cy="6" r="2" fill="#ec1f27"/></svg></span>
      <span>24/88 Harlow Rd<br>Glen Ashby VIC 3152</span>
    </div>
  </div>
</div></header>

<nav class="nav"><ul>
  <li class="active">Home</li><li>Tovi story</li><li>Electrical</li><li>Led Lighting</li><li>Solar Power</li><li>Our work</li><li>Contact us</li>
</ul></nav>

<section class="hero">
  <div class="photo" role="img" aria-label="Wind turbines and solar panels beside a city skyline under a red-tinted sky"></div>
  <h1>Want to <em>save</em> on power bills and do your part in<br>conserving <em>resources</em>?</h1>
  <div class="actions">
    <a class="btn ghost">Solar Power ➔</a>
    <a class="btn solid">Contact Us ➔</a>
  </div>
</section>

<section class="story"><div class="wrap">
  <h2 class="sec-title">The Tovi Story</h2>
  <p>Electrical and Energy Solutions are at the forefront of our company. Tovi Electrical has a long history in Electrical, LED Lighting and Solar Power and just like the Cougar, we will strive to be fierce &amp; agile in an effort to exceed our customer's expectations and develop stronger links with all our business partners &amp; community.</p>
  <a class="btn">Explore More ➔</a>
  <div class="cards">
    <div class="card" role="img" aria-label="Electrician wiring a switchboard" style="background:linear-gradient(160deg,#c9ccd1,#6f7680 60%,#3a4560)"><span class="label">Electrical</span></div>
    <div class="card" role="img" aria-label="Hanging LED pendant lights with plants" style="background:linear-gradient(170deg,#e9d6b4,#b98a55 55%,#6f5238)"><span class="label">Led Lighting</span></div>
    <div class="card" role="img" aria-label="Solar panel array against a blue sky" style="background:linear-gradient(200deg,#8fb2dc,#4b6e9a 50%,#2d3a52)"><span class="label hot">Solar Power</span></div>
  </div>
</div></section>

<section class="why"><div class="wrap">
  <div class="left">
    <h2 class="side-title">Why Choose Us</h2>
    <p>When you hire a Tovi Electrical Electrician you will get a professional and well-presented Electrician that comes skilled and ready to do the job.</p>
    <ul class="ticks">
      <li>Electrical Contracting</li><li>LED Lighting Upgrades</li><li>Solar Power</li><li>Security Systems</li><li>Fuse Box Repair &amp; Upgrades</li>
    </ul>
    <a class="btn">Read More ➔</a>
  </div>
  <div class="features">
    <div class="feature on"><span class="ico"><svg width="20" height="20" viewBox="0 0 20 20" fill="#fff"><circle cx="10" cy="6" r="4"/><path d="M2 19c0-5 4-7 8-7s8 2 8 7Z"/></svg></span>Professional service</div>
    <div class="feature"><span class="ico"><svg width="20" height="20" viewBox="0 0 20 20" fill="#fff"><path d="M2 9h4v9H2ZM7 9l4-7c2 0 2 2 1.5 4H17c1 0 2 1 1.6 2l-1.8 8c-.2.6-.8 1-1.4 1H7Z"/></svg></span>5-year workmanship<br>guarantee</div>
    <div class="feature"><span class="ico"><svg width="22" height="16" viewBox="0 0 22 16"><rect x="1" y="1" width="20" height="14" rx="2" fill="none" stroke="#fff" stroke-width="2"/><circle cx="11" cy="8" r="3" fill="#fff"/></svg></span>Value for Money</div>
    <div class="feature"><span class="ico"><svg width="18" height="18" viewBox="0 0 18 18"><path d="M2 16C2 7 7 2 16 2c0 9-5 14-14 14Zm0 0 8-8" fill="none" stroke="#fff" stroke-width="2"/></svg></span>Environmentally friendly</div>
    <div class="feature"><span class="ico"><svg width="20" height="20" viewBox="0 0 20 20"><rect x="2" y="3" width="15" height="15" rx="2" fill="none" stroke="#fff" stroke-width="2"/><path d="M6 10l3 3 9-10" fill="none" stroke="#fff" stroke-width="2"/></svg></span>Fully insured</div>
    <div class="feature"><span class="ico"><svg width="18" height="18" viewBox="0 0 18 18"><circle cx="9" cy="9" r="7" fill="#fff"/></svg></span>Tovi Electrical</div>
  </div>
</div></section>

<section class="clients"><div class="wrap">
  <h2 class="sec-title">What Our Clients Says</h2>
  <div class="avatar" role="img" aria-label="Client portrait"></div>
  <span class="arrow prev"><svg width="10" height="14" viewBox="0 0 10 14"><path d="M8 1 2 7l6 6" fill="none" stroke="#1e1f24" stroke-width="2"/></svg></span>
  <span class="arrow next"><svg width="10" height="14" viewBox="0 0 10 14"><path d="M2 1l6 6-6 6" fill="none" stroke="#fff" stroke-width="2"/></svg></span>
  <blockquote>I found Marcus to be well organised, punctual, professional and a good communicator. He did the job at a very reasonable price. A pleasure to deal with.</blockquote>
  <div class="who">- Lena P. -</div>
  <div class="where">Glen Ashby VIC</div>
</div></section>

<section class="works">
  <div class="wrap head">
    <h2 class="side-title">Our Works</h2>
    <a class="btn solid">View all work</a>
  </div>
  <div class="strip">
    <div role="img" aria-label="Empty warehouse with polished floor" style="background:linear-gradient(180deg,#8f969c,#5f656b)"></div>
    <div role="img" aria-label="Warehouse with LED high-bay lighting" style="background:linear-gradient(180deg,#a8aa9b,#6e6e5e)"></div>
    <div role="img" aria-label="Commercial lighting project"><div class="over" style="background:linear-gradient(180deg,#3c3d44,#24252b)">Rowan Hale<a class="btn ghost" style="height:26px;font-size:10px;padding:0 14px">View Project</a></div></div>
    <div role="img" aria-label="Factory workers on a production line" style="background:linear-gradient(180deg,#6d7f99,#3c4556)"></div>
    <div role="img" aria-label="Industrial workshop with orange cranes" style="background:linear-gradient(180deg,#6a8aa8,#8a6a3a)"></div>
  </div>
</section>

<section class="more"><div class="wrap">
  <div>
    <h2 class="side-title">Bright <em>Days</em> Ahead</h2>
    <ul class="ticks">
      <li>Bright days ahead when you take control, get off the grid and save money</li>
      <li>Bright days ahead when you get your electrical requirements fixed properly</li>
      <li>Bright days ahead when you upgrade to LED</li>
      <li>Bright days ahead when you choose to work with Tovi ( the cougar is a powerful animal)</li>
      <li>Catchy, trustworthy, reliable, strong</li>
    </ul>
    <a class="btn">Explore More ➔</a>
  </div>
  <div class="video">
    <span class="bar">Tovi 30 sec</span>
    <div class="screen">Tovi<small>Bright Days Ahead</small></div>
    <div class="progress"></div>
  </div>
</div></section>

<footer class="footer"><div class="wrap">
  <div class="col" style="width:200px">
    <h4>Quick Links</h4>
    <ul class="links"><li>Home</li><li class="active">Tovi Story</li><li>Portfolio</li><li>Our work</li><li>Contact Us</li></ul>
  </div>
  <div class="col" style="width:236px">
    <h4>Contact us</h4>
    <div>24/88 Harlow Rd Glen<br>Ashby VIC 3152</div>
    <div class="phone">Call Us: +139907</div>
    <div>service@tovielectrical.com.au</div>
  </div>
  <div class="col" style="width:298px">
    <h4>Newsletter Subscribe</h4>
    <div>Subscribe to our newsletter and we will<br>inform.</div>
    <div class="signup"><span>Email Address</span><b><svg width="14" height="14" viewBox="0 0 16 16"><path d="M1 7 15 1 10 15 7 9Z" fill="#fff"/></svg></b></div>
  </div>
  <div class="col">
    <h4>Follow US</h4>
    <div class="circles"><span></span><span class="on"></span><span></span></div>
  </div>
</div></footer>

<div class="bottom"><div class="wrap">
  <span>© Copyright 2017 Tovi Electrical. All Rights Reserved</span>
  <nav><span>Privacy</span><span>|</span><span>Terms and Conditions</span></nav>
</div></div>

</body>
</html>
```